New College Graduate Resume - Creative and unique design that stands out from the rest

Need creative resume design for recent college graduate who graduated from School of Music with a concentration in music composition and production. Striving for a contemporary layout/design that allows the resume to "be unique" and "stand out" but be polished and professional. Open to integrating moderate color/graphics as part of resume design but the design can be minus those attributes as well. Attached is raw content in 7 sections (name/contact info, education, highlights of qualifications, work experience, honors/awards, and professional affiliations). While the designer has full latitude over overall design which (section headers, font type, separation/spacing, use of bullets, justification of text, etc.) please maintain current order/sequence of the 7 sections.

Industry/Entity Type

School

Requirements
Must have
• Name (Tobias Garrick Elwin III) should be most prominent (bold/font size) compared to remainder of resume copy.
• Section headers should be prominent but less so when compared to name on resume.
• The attached file of resume content is provided as raw source copy and is NOT to be just copied and pasted into open fields as is. Expectation is each section of copy will be organized in a manner that is most visually appealing and may include bullets, appropriate spacing, etc.
Should not have
• The attached file of resume content is provided as source copy and is NOT to be just copied and pasted into open fields as is. Expectation is each section of copy will be organized in a manner that

```html
<!DOCTYPE html>
<html lang="en">
<head>
<meta charset="utf-8">
<title>Tobias Garrick Elwin III – Resume</title>
<link href="https://fonts.googleapis.com/css2?family=Oswald:wght@500&family=Fira+Sans:wght@400;500&display=swap" rel="stylesheet">
<style>
:root{
  --sidebar:#504d6d;
  --ink:#4b4868;
  --text:#2b2b33;
  --white:#ffffff;
}
*{margin:0;padding:0;box-sizing:border-box}
html,body{width:851px;height:1200px;overflow:hidden;background:var(--white)}
.resume{position:relative;width:851px;height:1200px;overflow:hidden;font-family:"Fira Sans",sans-serif;color:var(--text)}
.sidebar{position:absolute;left:0;top:0;width:314px;height:1200px;background:var(--sidebar);color:var(--white)}
.side-heading{position:absolute;left:30px;font-family:"Oswald",sans-serif;font-weight:500;font-size:34px;line-height:37px;text-transform:uppercase;letter-spacing:-0.3px;color:var(--white)}
.profile-text{position:absolute;left:32px;top:70px;width:255px;font-size:13.2px;line-height:17.7px;font-weight:400}
.square-list{position:absolute;list-style:none;font-size:13.2px;line-height:17.7px}
.square-list li{position:relative;padding-left:22px}
.square-list li::before{content:"";position:absolute;left:0;top:5px;width:8px;height:8px;background:var(--white)}
.qualifications{left:31px;top:380px}
.awards{left:29px;top:702px}
.awards li{padding-left:26px;margin-bottom:10px}
.awards li::before{top:calc(50% - 4px)}
.affiliations{left:29px;top:1007px}
.affiliations li{padding-left:26px;margin-bottom:7px}
.affiliations li::before{top:calc(50% - 4px)}

.name{position:absolute;left:342px;top:16px;font-family:"Oswald",sans-serif;font-weight:500;font-size:53px;line-height:66px;color:var(--ink);text-transform:uppercase;letter-spacing:-0.5px;white-space:nowrap;transform:scaleX(0.84);transform-origin:left center}
.contact{position:absolute;left:344px;top:84px;list-style:none;font-size:13.5px;line-height:17.5px}
.contact li{display:flex;align-items:center;gap:7px}
.contact svg{width:12px;height:12px;flex:none}
.main-heading{position:absolute;left:342px;font-family:"Oswald",sans-serif;font-weight:500;font-size:34px;line-height:40px;color:var(--ink);text-transform:uppercase;letter-spacing:-0.3px}
.edu-entry{position:absolute;left:380px;font-size:17px;line-height:22.7px}
.bullet{position:absolute;left:344px;width:8px;height:8px;background:var(--ink)}
.job{position:absolute;left:380px;width:455px;font-size:13.8px;line-height:18.6px}
.job-employer,.job-title{color:var(--ink);font-weight:500;font-size:14.5px}
.job-employer span{font-weight:400;color:var(--text)}
.duties{list-style:none;margin-top:10px;padding-left:34px}
.duties li{position:relative;padding-left:0}
.duties li::before{content:"";position:absolute;left:-19px;top:5px;width:8px;height:8px;background:var(--ink)}
</style>
</head>
<body>
<div class="resume">
  <aside class="sidebar">
    <h2 class="side-heading" style="top:24px">Profile</h2>
    <p class="profile-text">Recent graduate of a highly ranked university seeking opportunities to apply composition and production talents across a variety of music genres and other media. Expertise lies in delivering high quality sound design, editing, mixing, and recording. Excellent interpersonal skills and the ability to build strong relationships with people at all levels. Exceptionally motivated self-starter and creative problem solver who enjoys working collaboratively on teams.</p>

    <h2 class="side-heading" style="top:292px">Highlights of<br>Qualifications</h2>
    <ul class="square-list qualifications">
      <li>Media Production Software<br>(SessionPro 11)</li>
      <li>Sound Design</li>
      <li>Sound Acoustics</li>
      <li>Studio Recording</li>
      <li>Audio Editing</li>
      <li>Audio Mixing</li>
      <li>Analog/Digital board operation</li>
      <li>Music Arranging</li>
      <li>Music Composition</li>
      <li>Music Production</li>
      <li>Composing Sheet Music</li>
      <li>Singer-songwriter</li>
      <li>Rhythm guitarist</li>
    </ul>

    <h2 class="side-heading" style="top:653px">Honors/Awards</h2>
    <ul class="square-list awards">
      <li>Best Film and Score:<br>Frights and Themes 2015 Competition<br>(Bayview University)</li>
      <li>Walter B Ashcombe Scholar</li>
      <li>Best New Member,<br>Delta Rho Kappa Fraternity, Inc.</li>
      <li>Bayview University<br>Homecoming King, 2012</li>
    </ul>

    <h2 class="side-heading" style="top:918px">Professional<br>Affiliations</h2>
    <ul class="square-list affiliations">
      <li>Member, Guild of New<br>Composers Incorporated (GNC)</li>
      <li>Member, National Alliance of<br>Composers, Authors, and Publishers<br>(NACAP)</li>
      <li>Member, Sound Craft<br>Society (SCS)</li>
      <li>Member, Delta Rho Kappa<br>Fraternity, Incorporated</li>
    </ul>
  </aside>

  <main>
    <h1 class="name">Tobias Garrick Elwin III</h1>
    <ul class="contact">
      <li><svg viewBox="0 0 12 12"><rect x="0.5" y="0.5" width="11" height="11" fill="none" stroke="#4b4868"/><path d="M3 6 L6 3 L9 6 V9.5 H3 Z" fill="#4b4868"/></svg>218 Corvell Lane, Atlanta, Georgia&nbsp; 30309</li>
      <li><svg viewBox="0 0 12 12"><circle cx="6" cy="6" r="5.4" fill="none" stroke="#4b4868"/><rect x="4.2" y="3" width="3.6" height="6" rx="0.6" fill="none" stroke="#4b4868" stroke-width="0.9"/></svg>404-555-0186</li>
      <li><svg viewBox="0 0 12 12"><rect x="0.5" y="2.5" width="11" height="7" fill="none" stroke="#4b4868"/><path d="M0.5 2.5 L6 7 L11.5 2.5" fill="none" stroke="#4b4868"/></svg>tgelwin@mailbox.example</li>
    </ul>

    <h2 class="main-heading" style="top:180px">Education</h2>
    <span class="bullet" style="top:280px"></span>
    <div class="edu-entry" style="top:237px">Bayview University – Harlan School of Music<br>Coral Springs, Florida<br>Bachelor of Music – May 2016<br>Major: Media Writing and Production</div>
    <span class="bullet" style="top:385px"></span>
    <div class="edu-entry" style="top:353px">Linwood Preparatory Academy<br>College Park, Georgia<br>High School Diploma with Honors – May 2011</div>

    <h2 class="main-heading" style="top:462px">Work Experience</h2>

    <span class="bullet" style="top:519px"></span>
    <div class="job" style="top:513px">
      <div class="job-employer">Coastline Picture House (CPH)</div>
      <div>Miami, FL</div>
      <div>May 2014 – Present</div>
      <div class="job-title">Sound Engineer</div>
      <ul class="duties">
        <li>Edited and mixed recorded field audio to professional standards. Matched audio with motion picture video to create a seamless product.</li>
        <li>Recorded automated dialogue replacement (ADR) audio and integrated into motion picture video project using SessionPro 11.</li>
        <li>Recorded foley sound effects to be added to film, video, and other media in post-production.</li>
        <li>Composed and recorded original music to accompany various video projects.</li>
      </ul>
    </div>

    <span class="bullet" style="top:789px"></span>
    <div class="job" style="top:783px">
      <div class="job-employer">Brightmart Stores</div>
      <div>Atlanta, GA</div>
      <div>May 2013 - October 2013</div>
      <div class="job-title">Sales Associate</div>
      <div>Provided customer service, maintained a clean and organized work environment, assisted in sales, and performed cashier responsibilities.</div>
    </div>

    <span class="bullet" style="top:919px"></span>
    <div class="job" style="top:913px">
      <div class="job-employer">Peach State CAG <span>(Civic Action Group)</span></div>
      <div>Atlanta, GA</div>
      <div>June 2012 - August 2012</div>
      <div class="job-title">On-Site Promoter/Intern</div>
      <div>Promoted and advertised various campaigns and managed various office tasks, such as setting up site maps and organizing and sorting non-profit donations.</div>
    </div>

    <span class="bullet" style="top:1066px"></span>
    <div class="job" style="top:1060px">
      <div class="job-employer">Keystone Direct, Incorporated</div>
      <div>Atlanta, GA</div>
      <div>June 2011 – August 2011</div>
      <div class="job-title">Product Marketing Consultant</div>
      <div>Conducted direct sales and marketing of subsidiary product line through establishing a compelling value proposition, overcoming objections, and closing the sale.</div>
    </div>
  </main>
</div>
</body>
</html>
```